Web SITE design for new book

I need a unique design for a book my friend is releasing.

The home page needs to include:
A picture of the book
A spot for a video

Navigation:
Home
About the Book
Buy the Book
About the Author
Investing
Log In

The person awarded the project will also need to provide designs for the 5 other internal pages. They should be pretty straight forward.

Link to book design: https://www.filvantra.net/s/qmrt82kw7zpalvq/book-cover.png

Thanks!

```html
<!DOCTYPE html>
<html lang="en">
<head>
<meta charset="utf-8">
<title>The 5 Pitfalls – Home</title>
<link href="https://fonts.googleapis.com/css2?family=Open+Sans:wdth,wght@75..100,300..800&display=swap" rel="stylesheet">
<style>
:root{
  --surround:#565656;
  --gold:#b59b59;
  --gold-dark:#8d7843;
  --olive:#7d6e35;
  --white:#ffffff;
  --video-edge:#333333;
  --video-core:#3c3c3c;
  --play:#4a4a4a;
  --play-arrow:#6a6a6a;
  --footer:#3a3a3a;
  --icon-disc:#262626;
  --cta:#e8532b;
  --cover-light:#f3f3f4;
  --cover-shade:#d6d6d8;
}
*{margin:0;padding:0;box-sizing:border-box}
html,body{width:1200px;height:985px;overflow:hidden}
body{background:var(--surround);font-family:"Open Sans",Arial,sans-serif;position:relative}
.page{position:absolute;left:70px;top:5px;width:1045px;height:980px;background:var(--white)}
.site-header{position:absolute;left:0;top:0;width:1045px;height:131px;background:var(--gold)}
.brand{position:absolute;left:66px;top:24px;color:var(--white);line-height:24px}
.brand-name{font-size:20px;font-weight:400}
.brand-tagline{font-size:19px;font-weight:700;width:230px}
.login{position:absolute;left:907px;top:21px;display:flex;align-items:center;gap:10px;color:var(--white);font-size:14px;font-weight:600}
.login-box{width:20px;height:20px;border:3px solid #e8e0c8}
.main-nav{position:absolute;left:329px;top:80px;height:51px;display:flex;align-items:center}
.main-nav a{color:var(--white);text-decoration:none;font-size:19px;height:51px;line-height:51px}
.nav-home{background:var(--gold-dark);width:95px;text-align:center}
.nav-about{margin-left:12px}
.nav-buy{margin-left:22px}
.nav-author{margin-left:28px}
.nav-investing{margin-left:41px}
.hero{position:absolute;left:0;top:131px;width:1045px;height:597px}
.book-cover{position:absolute;left:40px;top:34px;width:357px;height:467px;background:linear-gradient(135deg,var(--cover-shade) 0%,var(--cover-light) 45%,var(--cover-shade) 100%)}
.video{position:absolute;left:465px;top:67px;width:549px;height:305px;background:var(--video-edge)}
.video-screen{position:absolute;left:57px;top:0;width:433px;height:305px;background:var(--video-core)}
.video-play{position:absolute;left:192px;top:110px}
.join{position:absolute;left:549px;top:400px;color:var(--olive);font-stretch:87.5%;font-size:50px;line-height:42px;white-space:nowrap;letter-spacing:-0.5px}
.join-light{font-weight:300}
.join strong{font-weight:700}
.join-line2{display:block;margin-left:10px;font-weight:700}
.cta{position:absolute;left:631px;top:522px;width:172px;height:38px;background:var(--cta);color:var(--white);font-size:15px;font-weight:700;text-align:center;line-height:38px;text-decoration:none}
.site-footer{position:absolute;left:0;top:728px;width:1045px;height:252px;background:var(--footer);color:var(--white)}
.feature{position:absolute;top:71px;display:flex;gap:12px}
.feature-icon{width:70px;height:70px;border-radius:50%;background:var(--icon-disc);flex:none;display:flex;align-items:center;justify-content:center;font-size:34px;font-weight:300;margin-top:4px}
.feature h3{font-size:20px;font-weight:700;line-height:24px}
.feature h3.small-caps{font-size:13px;text-transform:uppercase;line-height:24px}
.feature p{font-size:13px;line-height:17px;width:180px}
.feature-1{left:110px}
.feature-2{left:389px}
.feature-3{left:668px}
.copyright{position:absolute;left:704px;top:226px;font-size:12px;font-weight:600}
</style>
</head>
<body>
<div class="page">
  <header class="site-header">
    <div class="brand">
      <div class="brand-name">The 5 pitfalls</div>
      <div class="brand-tagline">Every saver meets and how to sidestep them</div>
    </div>
    <a class="login"><span class="login-box"></span>LOG IN</a>
    <nav class="main-nav">
      <a class="nav-home" href="#">Home</a>
      <a class="nav-about" href="#">About the Book</a>
      <a class="nav-buy" href="#">Buy the Book</a>
      <a class="nav-author" href="#">About the Author</a>
      <a class="nav-investing" href="#">Investing</a>
    </nav>
  </header>

  <section class="hero">
    <div class="book-cover" role="img" aria-label="Photo of the book The 5 Pitfalls"></div>

    <div class="video">
      <div class="video-screen">
        <svg class="video-play" width="82" height="82" viewBox="0 0 82 82" aria-label="Play video">
          <circle cx="41" cy="41" r="41" fill="var(--play)"/>
          <polygon points="31,23 31,59 61,41" fill="var(--play-arrow)"/>
        </svg>
      </div>
    </div>

    <h1 class="join"><span class="join-light">JOIN OUR </span><strong>INVESTING</strong><span class="join-line2">COMMUNITY</span></h1>
    <a class="cta" href="#">Buy the book NOW</a>
  </section>

  <footer class="site-footer">
    <div class="feature feature-1">
      <div class="feature-icon">$</div>
      <div><h3>Investing</h3><p>Lorem ipsum dolor sit amet, consectetur adscing elit. Vivamus aliquam velit.</p></div>
    </div>
    <div class="feature feature-2">
      <div class="feature-icon">$</div>
      <div><h3>Investing</h3><p>Lorem ipsum dolor sit amet, consectetur adscing elit. Vivamus aliquam velit.</p></div>
    </div>
    <div class="feature feature-3">
      <div class="feature-icon">?</div>
      <div><h3 class="small-caps">Surveys &amp; Petitions</h3><p>Lorem ipsum dolor sit amet, consectetur adscing elit. Vivamus aliquam velit.</p></div>
    </div>
    <div class="copyright">Copyright 2014 The 5 pitfalls</div>
  </footer>
</div>
</body>
</html>
```